Banner für Immobilienmakler
Zielgruppe
Immobilienmakler, Immobilienverkauf mit Herz,
Aufgabenstellung
Verkauf von Häusern und Wohnungen, der Banner soll an einen Balkon oder einen Zaun angebracht werden mit dem Hinweis, dass das Haus Zu verkaufen ist.
Maße ca. 76 x 244cm
Es darf gerne frech und modern sein mit einem witzigen einladenden Spruch sein, sollte aber auch ansonsten zu meinem chicen Style passen (siehe Homepage www.kranichhausverkauf.de) es soll sich abheben von anderen langweiligen Bannern.
Ggf soll die Plane auch noch an einem Tennisplatz angebracht werden

```html
<!DOCTYPE html>
<html lang="de">
<head>
<meta charset="utf-8">
<title>Banner – Kranich Immobilien</title>
<link href="https://fonts.googleapis.com/css2?family=Roboto:wght@300;400;500;700;900&display=swap" rel="stylesheet">
<style>
  :root {
    --stage: #929292;
    --ink: #262626;
    --band: #2b2b2b;
    --gold: #c8a664;
    --white: #ffffff;
    --wall-light: #f4f4f4;
    --wall-shade: #dcdcdc;
  }
  * { box-sizing: border-box; margin: 0; padding: 0; }
  html, body {
    width: 1200px; height: 720px; overflow: hidden;
    background: var(--stage);
    font-family: "Roboto", Arial, sans-serif;
  }
  .banner {
    position: absolute; left: 30px; top: 166px;
    width: 1140px; height: 388px;
    background: linear-gradient(135deg, var(--wall-light) 0%, #ececec 55%, var(--wall-shade) 100%);
    overflow: hidden;
  }
  .banner__photo {
    position: absolute; left: 0; top: 0;
    width: 360px; height: 306px;
    background: linear-gradient(160deg, #d9d3c8 0%, #b9a58a 45%, #8a6a4a 100%);
    clip-path: polygon(0 0, 349px 0, 295px 306px, 0 306px);
  }
  .brand-seal {
    position: absolute; left: 346px; top: 34px;
    width: 142px; height: 142px; border-radius: 50%;
    background: var(--band);
    display: flex; align-items: center; justify-content: center;
    text-align: center;
  }
  .brand-seal__name {
    color: var(--white); font-weight: 500; font-size: 17px;
    line-height: 1.2; letter-spacing: 1px; text-transform: uppercase;
  }
  .headline {
    position: absolute; left: 511px; top: 58px; color: var(--ink);
  }
  .headline__lead {
    display: block; font-weight: 400; font-size: 54px; line-height: 60px;
    letter-spacing: -0.5px;
  }
  .headline__main {
    display: block; margin-left: 20px; font-weight: 700; font-size: 58px;
    line-height: 66px; letter-spacing: -1px;
  }
  .offer-bar {
    position: absolute; left: 346px; top: 206px;
    width: 794px; height: 50px;
    background: var(--band);
    clip-path: polygon(14px 0, 100% 0, 100% 100%, 0 100%);
    display: flex; align-items: center; padding-left: 52px;
    color: var(--white); font-size: 32px; font-weight: 400;
    letter-spacing: -0.3px; white-space: nowrap;
  }
  .offer-bar__accent { color: var(--gold); font-weight: 700; margin-left: 10px; }
  .contact-band {
    position: absolute; left: 0; bottom: 0; width: 100%; height: 82px;
    background: var(--band);
    display: flex; align-items: center; justify-content: space-between;
    padding: 0 26px 0 24px;
    color: var(--white); white-space: nowrap;
  }
  .contact { display: flex; align-items: center; gap: 12px; font-size: 24px; font-weight: 500; }
  .contact--phone { font-size: 26px; font-weight: 700; }
  .contact__icon { width: 22px; height: 22px; flex: none; }
</style>
</head>
<body>
  <div class="banner">
    <div class="banner__photo" role="img" aria-label="Foto: Familie spielt beim Umzug mit einem Kind im Umzugskarton in einer hellen Wohnung"></div>

    <div class="brand-seal">
      <span class="brand-seal__name">Kranich<br>Immobilien</span>
    </div>

    <h1 class="headline">
      <span class="headline__lead">Lust auf einen</span>
      <span class="headline__main">TAPETENWECHSEL?</span>
    </h1>

    <div class="offer-bar">DIESE IMMOBILIE STEHT <span class="offer-bar__accent">ZUM VERKAUF!</span></div>

    <div class="contact-band">
      <div class="contact contact--phone">
        <svg class="contact__icon" viewBox="0 0 24 24"><path fill="#c8a664" d="M6.6 10.8c1.4 2.8 3.8 5.1 6.6 6.6l2.2-2.2c.3-.3.7-.4 1-.2 1.1.4 2.3.6 3.6.6.6 0 1 .4 1 1V20c0 .6-.4 1-1 1C10.6 21 3 13.4 3 4c0-.6.4-1 1-1h3.5c.6 0 1 .4 1 1 0 1.3.2 2.5.6 3.6.1.3 0 .7-.2 1l-2.3 2.2z"/></svg>
        <span>02241 / 47 31 206</span>
      </div>
      <div class="contact">
        <svg class="contact__icon" viewBox="0 0 24 24"><rect x="2" y="5" width="20" height="14" fill="#c8a664"/><path d="M2 5l10 8 10-8" fill="none" stroke="#2b2b2b" stroke-width="1.6"/></svg>
        <span>info@kranichhausverkauf.de</span>
      </div>
      <div class="contact">
        <svg class="contact__icon" viewBox="0 0 24 24" fill="none" stroke="#c8a664" stroke-width="1.8"><circle cx="12" cy="12" r="10"/><ellipse cx="12" cy="12" rx="4.5" ry="10"/><path d="M2 12h20M4 7h16M4 17h16"/></svg>
        <span>www.kranichhausverkauf.de</span>
      </div>
    </div>
  </div>
</body>
</html>
```